Cover page for Master's thesis (in Word)

I need a cover page for my Master's thesis which I am currently working on. The topic is "Mobile Usability" so MOBILE should also be the overall theme of the design. The primary color should be blue since my school and the company where I am writing my thesis are primarily using blue in their Corporate Identities.
I enclosed a template in Word and pdf with all the necessary information that must be included on the cover page. Please also consider and adhere to the page margins and the printable areas set in the Word template and please use Verdana for the mandatory text elements mentioned. The topic font can be different and it's up to you.
The design shouldn't be too fancy since this is a dissertation and not an ad for an Quince product. I would prefer a simple, flat, modern and professional design with flat colors. I also attached the logo of my University and my company (which should of course be included) as well as a leaflet of my Uni for inspiration.

If you have any questions or if you need more information or material, just drop me a line.

Thanks a lot in advance!
Torben

```html
<!DOCTYPE html>
<html lang="en">
<head>
<meta charset="utf-8">
<title>Master's Thesis Cover – Mobile Usability</title>
<link rel="stylesheet" href="https://fonts.googleapis.com/css2?family=Open+Sans:wght@600&family=Noto+Sans:wght@400;700&display=swap">
<style>
  :root {
    --stage: #fdfcf8;
    --paper: #ffffff;
    --blue: #046eab;
    --blue-dark: #0565a0;
    --ink: #000000;
    --text: #1a1a1a;
    --grey: #7a7a7a;
    --white: #ffffff;
  }
  * { margin: 0; padding: 0; box-sizing: border-box; }
  html, body { width: 1200px; height: 1000px; overflow: hidden; background: var(--stage); }
  body { position: relative; font-family: Verdana, "Noto Sans", sans-serif; color: var(--text); }

  .cover {
    position: absolute; top: 149px; width: 522px; height: 742px;
    background: var(--paper);
    box-shadow: 0 2px 8px rgba(0,0,0,0.12);
    overflow: hidden;
  }
  .cover--full-blue { left: 56px; }
  .cover--band { left: 619px; }

  .cover > * { position: absolute; }
  .blue-field { left: 0; right: 0; background: var(--blue); }
  .cover--full-blue .blue-field { top: 115px; bottom: 0; }
  .cover--band .blue-field { top: 107px; height: 498px; }

  .school-name {
    left: 40px; color: var(--blue); font-size: 17px; line-height: 1.1;
    font-family: Verdana, "Noto Sans", sans-serif;
  }
  .cover--full-blue .school-name { top: 60px; }
  .cover--band .school-name { top: 60px; }

  .partner {
    display: flex; align-items: center; gap: 6px;
    font-size: 13px; font-weight: 700; letter-spacing: 0.5px;
  }
  .partner .mark { width: 10px; height: 10px; }
  .cover--full-blue .partner { left: 258px; top: 74px; color: var(--grey); }
  .cover--full-blue .partner .mark { background: var(--grey); }
  .cover--band .partner { left: 330px; top: 66px; color: var(--blue); }
  .cover--band .partner .mark { background: var(--blue); }

  .rule { height: 2px; background: var(--ink); }
  .thesis-label { left: 0; right: 0; text-align: center; color: var(--white); font-size: 11px; letter-spacing: 0.3px; }

  .title { left: 0; }
  .title text { font-family: "Open Sans", sans-serif; font-weight: 600; font-size: 64px; }
  .title .word-dark { fill: var(--ink); }
  .title .word-light { fill: var(--white); }

  .subtitle {
    left: 0; right: 0; text-align: center; color: var(--white);
    font-size: 20px; line-height: 25px; letter-spacing: 0.4px;
  }
  .byline { left: 0; right: 0; text-align: center; color: var(--white); }
  .byline .by { font-size: 10px; display: block; margin-bottom: 3px; }
  .byline .author { font-size: 19px; letter-spacing: 0.3px; }

  .device-art { left: 201px; top: 323px; width: 142px; height: 169px; border-radius: 8px;
    background: linear-gradient(160deg, #ffffff 0%, #e4eef6 100%); opacity: 0.92; }

  .facts { font-size: 11px; letter-spacing: 0.3px; color: var(--text); }
  .fact { display: flex; align-items: center; gap: 7px; white-space: nowrap; }
  .fact::before { content: ""; width: 10px; height: 10px; background: var(--ink); flex: none; }
  .cover--band .fact::before { background: var(--blue); }

  .dates { font-size: 11px; line-height: 13px; letter-spacing: 0.3px; color: var(--text); display: grid; grid-template-columns: 121px auto; }
</style>
</head>
<body>

<!-- Variant A: full blue body -->
<section class="cover cover--full-blue">
  <div class="blue-field"></div>
  <div class="school-name">Hochschule<br>Lindenau</div>
  <div class="partner"><span class="mark"></span>POINTWISE</div>

  <div class="rule" style="left:38px; top:178px; width:161px;"></div>
  <div class="rule" style="left:326px; top:178px; width:159px;"></div>
  <div class="thesis-label" style="top:172px;">MASTER`S THESIS</div>

  <svg class="title" style="top:190px;" width="522" height="70" viewBox="0 0 522 70">
    <text x="30" y="56" textLength="465" lengthAdjust="spacingAndGlyphs"><tspan class="word-dark">MOBILE</tspan><tspan class="word-light">USABILITY</tspan></text>
  </svg>
  <div class="rule" style="left:30px; top:258px; width:455px;"></div>
  <div class="subtitle" style="top:266px;">Analysis of the mobile application portfolio<br>of XXXXX Ltd.</div>

  <div class="byline" style="top:540px;"><span class="by">By</span><span class="author">Torben Brandt</span></div>

  <div class="facts" style="left:144px; top:622px;">
    <div class="fact" style="margin-bottom:7px;">Matriculation Number: 000XXXXX</div>
    <div class="fact">Degree Program: Marketing / Sales / Media</div>
  </div>

  <div class="dates" style="left:142px; top:664px;">
    <span>Issued on</span><span>06.11.2013</span>
    <span>Submitted on</span><span>07.04.2014</span>
    <span>First Examiner</span><span>Prof. Dr. Lena Hartwig</span>
    <span>Second Examiner</span><span>Prof. Dr. Jonas Richter</span>
  </div>
</section>

<!-- Variant B: blue band with white footer -->
<section class="cover cover--band">
  <div class="blue-field"></div>
  <div class="school-name">Hochschule<br>Lindenau</div>
  <div class="partner"><span class="mark"></span>POINTWISE</div>

  <div class="rule" style="left:40px; top:147px; width:161px;"></div>
  <div class="rule" style="left:327px; top:147px; width:163px;"></div>
  <div class="thesis-label" style="top:141px;">MASTER`S THESIS</div>

  <svg class="title" style="top:155px;" width="522" height="70" viewBox="0 0 522 70">
    <text x="32" y="56" textLength="465" lengthAdjust="spacingAndGlyphs"><tspan class="word-dark">MOBILE</tspan><tspan class="word-light">USABILITY</tspan></text>
  </svg>
  <div class="rule" style="left:38px; top:225px; width:452px;"></div>
  <div class="subtitle" style="top:233px;">Analysis of the mobile application portfolio<br>of XXXXX Ltd.</div>

  <div class="device-art" role="img" aria-label="Flat white outline illustration of a tablet with a smartphone beside it"></div>

  <div class="byline" style="top:529px;"><span class="by">By</span><span class="author">Torben Brandt</span></div>

  <div class="facts" style="left:64px; top:627px;">
    <div class="fact">Surname, Name: Torben Brandt</div>
  </div>
  <div class="facts" style="left:276px; top:627px;">
    <div class="fact">Matriculation Number: 000XXXXX</div>
  </div>
  <div class="facts" style="left:142px; top:647px;">
    <div class="fact">Degree Program: Marketing / Sales / Media</div>
  </div>

  <div class="dates" style="left:137px; top:669px;">
    <span>Issued on</span><span>06.11.2013</span>
    <span>Submitted on</span><span>07.04.2014</span>
    <span>First Examiner</span><span>Prof. Dr. Lena Hartwig</span>
    <span>Second Examiner</span><span>Prof. Dr. Jonas Richter</span>
  </div>
</section>

</body>
</html>
```